Business Card Design

Take existing logo/brand and develop business card for sales team.
We have two separate brands and require a business card for each.

1. VoxHarbor
2. MyNimbusLinko

Refer to our websites www.voxharbor.com.au and www.mynimbuslinko.com.au for designs currently implemented and in the marketplace.

Both cards are brands of our parent company Quorvane Systems Pty Ltd - an Australian Telecommunications company in the medium business sector. We have only business customers, no retail/residential consumers.

Target Market(s)

Australian Business - small to medium enterprise

Industry/Entity Type

Business

Contact Information for Business Card

Ted Ramsell
Sales Director
Mobile: +61 428 163 907
Direct: +61 3 9172 5836
Email: ted@voxharbor.com.au
VoxHarbor (a brand of Quorvane Systems Pty Ltd)

Ted Ramsell
Sales Director
Mobile: +61 428 163 907
Direct: +61 3 9172 5836
Email: ted@mynimbuslinko.com.au
MyNimbusLinko (a brand of Quorvane Systems Pty Ltd)

Font styles to use
Sans Serif
Other font styles liked:
• Roboto Condensed, Open Sans

Requirements
Must have
• Clean lines, crisp fonts - suggest Roboto Condensed or similar.
• Must be easy to read and clear.
• Brand colour #0C8CCD
• Two colour maximum
Nice to have
• Modern, intellectual and unique design.
Should not have
• No die cuts
• No copies or rip-offs of other designs

```html
<!DOCTYPE html>
<html lang="en">
<head>
<meta charset="utf-8">
<title>MyNimbusLinko Business Card</title>
<link rel="stylesheet" href="https://fonts.googleapis.com/css2?family=Roboto:wght@300;400;500&display=swap">
<style>
  :root {
    --brand-blue: #0c8ccd;
    --brand-blue-deep: #0a6fb0;
    --ink: #3a3a3c;
    --ink-soft: #6b6b6e;
    --slate: #4a4a4c;
    --card: #f6f6f6;
    --backdrop: #e4e4e6;
  }
  * { margin: 0; padding: 0; box-sizing: border-box; }
  html, body {
    width: 1200px;
    height: 900px;
    overflow: hidden;
    background: var(--backdrop);
    font-family: "Roboto", Arial, sans-serif;
    color: var(--ink);
  }
  .canvas {
    position: relative;
    width: 1200px;
    height: 900px;
  }
  .card {
    position: absolute;
    width: 600px;
    height: 343px;
    background: var(--card);
    box-shadow: 0 2px 6px rgba(0,0,0,0.12);
    overflow: hidden;
  }
  .card--front { left: 90px; top: 100px; }
  .card--back { left: 510px; top: 460px; }

  /* Front */
  .front-feature {
    position: absolute;
    left: 0; top: 0;
    width: 200px; height: 343px;
    background: linear-gradient(160deg, var(--brand-blue) 0%, var(--brand-blue-deep) 55%, var(--slate) 100%);
  }
  .front-wordmark {
    position: absolute;
    right: 40px;
    bottom: 70px;
    font-size: 40px;
    font-weight: 300;
    color: var(--ink);
    letter-spacing: -0.5px;
  }

  /* Back */
  .brand-lockup {
    position: absolute;
    left: 228px;
    top: 52px;
    display: flex;
    align-items: center;
    gap: 10px;
  }
  .brand-mark {
    width: 40px; height: 40px;
    background: var(--brand-blue);
  }
  .brand-name {
    font-size: 34px;
    font-weight: 300;
    color: var(--ink);
    letter-spacing: -0.5px;
  }
  .web {
    position: absolute;
    right: 30px;
    top: 114px;
    font-size: 13px;
    font-weight: 300;
    color: var(--ink-soft);
  }
  .rule {
    position: absolute;
    height: 1px;
    background: var(--brand-blue);
  }
  .rule--top { left: 300px; right: 30px; top: 136px; }
  .rule--bottom { left: 40px; width: 380px; top: 318px; }

  .person {
    position: absolute;
    left: 40px;
    top: 128px;
  }
  .person-name {
    font-size: 15px;
    font-weight: 500;
    text-transform: uppercase;
    color: var(--ink);
  }
  .person-role {
    font-size: 13px;
    font-weight: 300;
    color: var(--ink-soft);
    margin-top: 3px;
  }
  .contacts {
    position: absolute;
    left: 40px;
    top: 200px;
    list-style: none;
    font-size: 13px;
    font-weight: 300;
    line-height: 19px;
    color: var(--ink-soft);
  }
  .contacts .key {
    display: inline-block;
    width: 16px;
    font-weight: 500;
    color: var(--brand-blue);
  }
  .company {
    position: absolute;
    left: 40px;
    top: 272px;
    font-size: 13px;
    line-height: 18px;
    font-weight: 300;
    color: var(--ink-soft);
  }
  .company strong {
    display: block;
    font-weight: 500;
    color: var(--ink);
  }
</style>
</head>
<body>
<main class="canvas">

  <section class="card card--front" aria-label="Card front">
    <div class="front-feature" role="img" aria-label="Brand graphic of blue and slate blocks"></div>
    <div class="front-wordmark">mynimbuslinko</div>
  </section>

  <section class="card card--back" aria-label="Card back">
    <div class="brand-lockup">
      <span class="brand-mark"></span>
      <span class="brand-name">mynimbuslinko</span>
    </div>
    <div class="web">www.mynimbuslinko.com.au</div>
    <div class="rule rule--top"></div>

    <div class="person">
      <div class="person-name">Ted Ramsell</div>
      <div class="person-role">Sales Director</div>
    </div>

    <ul class="contacts">
      <li><span class="key">E</span>ted@mynimbuslinko.com.au</li>
      <li><span class="key">C</span>+61 428 163 907</li>
      <li><span class="key">O</span>+61 3 9172 5836</li>
    </ul>

    <div class="company">
      <strong>MyNimbusLinko</strong>
      a brand of Quorvane Systems Pty Ltd
    </div>
    <div class="rule rule--bottom"></div>
  </section>

</main>
</body>
</html>
```